■依頼の目的/概要
社内活性化目的のポスター制作をお願いしたいです。

■依頼詳細
全社内向けに、部署のミッションを周知するためのポスター制作をお願いいたします。チーム全体のメッセージだけでなく、メンバーそれぞれの熱い思いが伝わる一枚を制作していただきたいです!
※構成は中心に代表者を置き、その周りに添付ファイルのようにメンバー個人写真・目標を入れます。
ポスターのPDFとai(もしくはPSD)データの提出をお願いいたします。

▼レギュレーション
・部署名、部署の半期目標と個人目標・顔写真を入れる
・サイズ:A0もしくはA1
・PDFは塗りたし上下左右3mmを入れる

■重視する点
過去・現在までにデザインの経験のある方を希望致します。

その他何かご不明な点がございましたら、お気軽にご質問下さい。
よろしくお願いいたします。
■依頼の目的/概要
社内活性化目的のポスター制作をお願いしたいです。

■依頼詳細

▼レギュレーション
・部署名、部署の半期目標と個人目標・顔写真を入れる
・サイズ:A0もしくはA1
・PDFは塗りたし上下左右3mmを入れる

■重視する点

よろしくお願いいたします。

遠くから見ても視認性が高く、インパクトのある作品でした。

この度はコンペのご参加ありがとうございました。
機会がございましたらまたお願いいたします。

```html
<!DOCTYPE html>
<html lang="ja">
<head>
<meta charset="UTF-8">
<title>今期のチーム目標 ポスター</title>
<link href="https://fonts.googleapis.com/css2?family=Oswald:wght@500;600&family=Noto+Sans+JP:wght@400;500;700;900&display=swap" rel="stylesheet">
<style>
  :root {
    --paper: #ffffff;
    --orange: #ec6a3c;
    --navy: #1f2f6e;
    --blue-deep: #223a78;
    --blue-mid: #4f68aa;
    --blue-soft: #8fa2d3;
    --blue-light: #d3dcf1;
  }
  html, body {
    margin: 0; padding: 0;
    width: 846px; height: 1200px;
    overflow: hidden;
    background: var(--paper);
  }
  .poster {
    position: relative;
    width: 846px; height: 1200px;
    background: var(--paper);
    font-family: "Noto Sans JP", sans-serif;
    color: var(--navy);
    overflow: hidden;
  }

  /* duotone portrait areas */
  .portrait {
    position: absolute;
    background:
      radial-gradient(ellipse 38% 46% at 50% 42%, var(--blue-light) 0%, rgba(211,220,241,0) 70%),
      radial-gradient(ellipse 60% 40% at 50% 100%, var(--blue-mid) 0%, rgba(79,104,170,0) 75%),
      linear-gradient(160deg, var(--blue-soft) 0%, var(--blue-mid) 50%, var(--blue-deep) 100%);
  }
  .portrait--top-left     { left: 136px; top: 79px;  width: 198px; height: 204px; }
  .portrait--top-right    { left: 353px; top: 23px;  width: 368px; height: 302px; }
  .portrait--leader       { left: 249px; top: 334px; width: 421px; height: 440px; }
  .portrait--bottom-left  { left: 113px; top: 673px; width: 283px; height: 262px; }
  .portrait--bottom-right { left: 429px; top: 700px; width: 292px; height: 247px; }

  .frame {
    position: absolute;
    left: 113px; top: 262px; width: 628px; height: 426px;
    border: 2px solid var(--orange);
  }

  .headline {
    position: absolute;
    margin: 0;
    font-family: "Oswald", sans-serif;
    font-weight: 600;
    font-size: 118px;
    line-height: 1;
    letter-spacing: 0;
    color: var(--orange);
    white-space: nowrap;
  }
  .headline--team { left: 138px; top: 270px; }
  .headline--for  { left: 138px; top: 424px; }
  .headline--term { left: 138px; top: 582px; }

  .member-tag {
    position: absolute;
    font-family: "Oswald", sans-serif;
    font-weight: 500;
    font-size: 17px;
    line-height: 1.1;
    letter-spacing: 1px;
    color: var(--orange);
    white-space: nowrap;
  }
  .member-tag small {
    display: block;
    font-family: "Noto Sans JP", sans-serif;
    font-size: 7px;
    letter-spacing: 0;
    margin-top: 3px;
  }
  .member-tag--top-left  { left: 56px;  top: 196px; }
  .member-tag--leader    { left: 290px; top: 410px; color: var(--paper); }
  .member-tag--bottom-right { left: 565px; top: 886px; }
  .member-tag--top-right {
    left: 728px; top: 36px;
    writing-mode: vertical-rl;
  }
  .member-tag--bottom-left {
    left: 28px; top: 720px;
    writing-mode: vertical-rl;
    transform: rotate(180deg);
  }

  .goal-note {
    position: absolute;
    font-size: 9px;
    line-height: 1.5;
    font-weight: 500;
    padding: 5px 6px;
    border: 1px solid var(--paper);
    color: var(--paper);
  }
  .goal-note--top-left     { left: 272px; top: 36px;  width: 40px; border-color: var(--orange); color: var(--orange); background: var(--paper); }
  .goal-note--top-right    { left: 392px; top: 262px; width: 58px; }
  .goal-note--leader       { left: 522px; top: 452px; width: 74px; }
  .goal-note--bottom-left  { left: 300px; top: 785px; width: 64px; }
  .goal-note--bottom-right { left: 445px; top: 835px; width: 62px; }

  .team-goal {
    position: absolute;
    left: 85px; width: 676px; top: 962px;
    text-align: center;
  }
  .team-goal__title {
    margin: 0;
    font-size: 36px;
    font-weight: 900;
    line-height: 1.2;
    letter-spacing: 2px;
  }
  .team-goal__rule {
    width: 520px; height: 2px;
    margin: 6px auto 8px;
    background: var(--navy);
  }
  .team-goal__name {
    margin: 0;
    font-size: 20px;
    font-weight: 700;
    line-height: 1.2;
  }
  .team-goal__body {
    margin: 14px 0 0;
    text-align: left;
    font-size: 9px;
    line-height: 1.75;
  }
</style>
</head>
<body>
  <main class="poster">
    <div class="portrait portrait--top-left" role="img" aria-label="眼鏡をかけたメンバーのポートレート写真(青のデュオトーン)"></div>
    <div class="portrait portrait--top-right" role="img" aria-label="女性メンバーのポートレート写真(青のデュオトーン)"></div>
    <div class="portrait portrait--leader" role="img" aria-label="チーム代表者の笑顔のポートレート写真(青のデュオトーン)"></div>
    <div class="portrait portrait--bottom-left" role="img" aria-label="笑顔の男性メンバーのポートレート写真(青のデュオトーン)"></div>
    <div class="portrait portrait--bottom-right" role="img" aria-label="笑顔の女性メンバーのポートレート写真(青のデュオトーン)"></div>

    <div class="frame"></div>

    <h1 class="headline headline--team">TEAM GOALS</h1>
    <p class="headline headline--for">FOR</p>
    <p class="headline headline--term">THIS TERM</p>

    <div class="member-tag member-tag--top-left">AKIKO MORITA<br>SALES TEAM<small>営業部 2年目</small></div>
    <div class="member-tag member-tag--leader">AKIKO MORITA<br>SALES TEAM<small>営業部 リーダー</small></div>
    <div class="member-tag member-tag--top-right">AKIKO MORITA</div>
    <div class="member-tag member-tag--bottom-left">AKIKO MORITA</div>
    <div class="member-tag member-tag--bottom-right">AKIKO MORITA<br>SALES TEAM</div>

    <div class="goal-note goal-note--top-left">新規顧客を倍に</div>
    <div class="goal-note goal-note--top-right">お客様の声を形にする</div>
    <div class="goal-note goal-note--leader">チーム全員で売上を一段アップする</div>
    <div class="goal-note goal-note--bottom-left">毎週の提案数を伸ばす</div>
    <div class="goal-note goal-note--bottom-right">信頼される担当になる</div>

    <section class="team-goal">
      <h2 class="team-goal__title">今期のチーム目標</h2>
      <div class="team-goal__rule"></div>
      <p class="team-goal__name">チーム名</p>
      <p class="team-goal__body">ここに今期のチーム目標の文章が入ります。この文章はダミーです。ここに今期のチーム目標の文章が入ります。この文章はダミーです。ここに今期のチーム目標の文章が入ります。この文章はダミーです。ここに今期のチーム目標の文章が入ります。この文章はダミーです。ここに今期のチーム目標の文章が入ります。この文章はダミーです。ここに今期のチーム目標の文章が入ります。この文章はダミーです。</p>
    </section>
  </main>
</body>
</html>
```